International Trade Consulting Firm Seeks Quality Newsletter Design

Our company provides consulting services to Pinnacle 300 type companies. We compete with the largest consulting companies in the world. However, we have the highest level of expertise in the industry and need to look the most professional and high end. We have very relevant and important information to provide our customers about their compliance and projects. We will have the winning design coded to be an e-newsletter, so it needs to be one page. We want to keep our company colors and logo design in the newsletter, they are attached. We DO NOT want it to look like a mini-version of our website. We want a fresh look to this marketing piece. Newsletter will need to include title, possible sub-heading, space for a feature story, 2 other stories included, and space on either the left or right for short cuts, links or highlights of other articles. Contents/'In this issue' section, about us or branding area, section for relevant links, etc...
Target Market(s)
Pinnacle 300 companies, High-level management
Industry/Entity Type
Marketing

```html
<!DOCTYPE html>
<html lang="en">
<head>
<meta charset="utf-8">
<title>Harborline Insider Newsletter</title>
<link href="https://fonts.googleapis.com/css2?family=Arimo:wght@400;700&family=Open+Sans:wght@400&display=swap" rel="stylesheet">
<style>
  :root {
    --page-bg: #ffffff;
    --masthead-bg: #000000;
    --brand-green: #4f9a3f;
    --masthead-text: #ffffff;
    --panel-bg: #eceef2;
    --sidebar-bg: #dde1e7;
    --info-bg: #d6dbe2;
    --bar-top: #dde2ea;
    --bar-bottom: #aeb6c4;
    --button-top: #a0a9b9;
    --button-bottom: #6f7b90;
    --heading-text: #26365a;
    --body-text: #4c5463;
    --muted-text: #717b8c;
    --rule: #c9ced7;
    --divider: #f7f8fa;
    --photo-fill: #b9c3cf;
  }
  * { box-sizing: border-box; margin: 0; padding: 0; }
  html, body {
    width: 1200px; height: 1000px; overflow: hidden;
    background: var(--page-bg);
    font-family: "Arimo", Arial, sans-serif;
    color: var(--body-text);
  }
  .newsletter { position: relative; width: 1200px; height: 1000px; }
  .block { position: absolute; }

  .masthead {
    left: 352px; top: 2px; width: 626px; height: 85px;
    background: var(--masthead-bg);
  }
  .brand-name {
    position: absolute; left: 26px; top: 27px; width: 190px;
    font-family: "Arimo", Arial, sans-serif; font-weight: 700;
    font-size: 15px; line-height: 17px; letter-spacing: 0.5px;
    color: var(--brand-green); text-transform: uppercase;
  }
  .issue-title {
    position: absolute; left: 262px; top: 22px; width: 340px;
    font-family: "Open Sans", Arial, sans-serif; font-size: 31px; font-weight: 400;
    line-height: 40px; color: var(--masthead-text); text-align: center;
  }

  .bar {
    position: absolute;
    background: linear-gradient(var(--bar-top), var(--bar-bottom));
    border-bottom: 1px solid #9aa3b2;
    display: flex; align-items: center; justify-content: space-between;
    padding: 0 18px;
    color: var(--heading-text);
  }
  .bar h2 { font-weight: 400; font-size: 16.5px; }
  .bar--small h2 { font-size: 13px; letter-spacing: 0.3px; }
  .panel { position: absolute; background: var(--panel-bg); border-bottom: 2px solid #fff; }
  .panel p { font-size: 11px; line-height: 17.2px; letter-spacing: 0.3px; }
  .story { padding: 18px 40px 0 22px; }
  .story p + p { margin-top: 8px; }
  .photo {
    float: left; margin: 2px 20px 4px 2px;
    border: 3px solid #fff;
    background: var(--photo-fill);
  }
  .story--compact { padding: 12px 28px 0 22px; }
  .story--compact p { font-size: 9.6px; line-height: 11.4px; letter-spacing: 0.35px; }
  .story--compact p + p { margin-top: 5px; }
  .bullets { list-style: none; padding: 12px 36px 0 22px; }
  .bullets li {
    position: relative; padding-left: 12px;
    font-size: 9.6px; line-height: 11.4px; letter-spacing: 0.35px; margin-bottom: 8px;
  }
  .bullets li::before {
    content: ""; position: absolute; left: 0; top: 4px;
    width: 4px; height: 4px; border-radius: 50%; border: 1px solid #8a93a3;
  }

  .divider {
    left: 352px; top: 610px; width: 626px; height: 4px;
    background: var(--divider); border-top: 1px solid #d5d9df; border-bottom: 1px solid #d5d9df;
  }

  .contents { left: 766px; top: 134px; width: 209px; }
  .contents li {
    list-style: none; height: 32px; background: var(--sidebar-bg);
    border-bottom: 1px solid #f4f5f7; padding-left: 23px;
    font-size: 11px; line-height: 32px; letter-spacing: 0.2px; color: var(--heading-text); position: relative;
  }
  .contents li::before {
    content: ""; position: absolute; left: 11px; top: 14px;
    width: 3px; height: 3px; border-radius: 50%; border: 1px solid #8a93a3;
  }
  .news-item {
    position: absolute; left: 766px; width: 209px;
    background: var(--sidebar-bg); padding: 16px 22px 0 16px;
    border-bottom: 2px solid #f4f5f7;
  }
  .news-item h3 { font-size: 10.5px; line-height: 14px; font-weight: 700; letter-spacing: 0.2px; color: #4a5466; margin-bottom: 8px; }
  .news-item p { font-size: 11px; line-height: 15.6px; letter-spacing: 0.3px; }

  .action {
    position: absolute; left: 766px; width: 209px; height: 43px;
    background: linear-gradient(var(--button-top), var(--button-bottom));
    display: flex; align-items: center; justify-content: space-between;
    padding: 0 18px; color: #fff; font-size: 15px; letter-spacing: 0.3px;
    border-bottom: 2px solid #5f6b7f;
  }

  .signup-note {
    position: absolute; left: 766px; top: 603px; width: 209px; height: 349px;
    background: var(--info-bg); padding: 9px 16px;
    font-size: 8px; line-height: 9.6px; letter-spacing: 0.3px; color: var(--muted-text);
  }
  .signup-note strong { color: #5a6476; }

  .legal {
    position: absolute; left: 356px; top: 958px; width: 619px; height: 32px;
    background: var(--panel-bg); border: 1px solid var(--rule);
    text-align: center; font-size: 7.8px; line-height: 10.5px; letter-spacing: 0.3px; color: var(--muted-text);
    padding-top: 1px;
  }
  .legal a { color: #333; font-weight: 700; }
</style>
</head>
<body>
<div class="newsletter">

  <header class="block masthead">
    <div class="brand-name">Harborline Trade Advisors</div>
    <h1 class="issue-title">HARBORLINE INSIDER</h1>
  </header>

  <div class="bar" style="left:356px;top:90px;width:406px;height:43px;"><h2>Me lius quod ii legunt saepius claritas</h2></div>
  <section class="panel" style="left:356px;top:133px;width:406px;height:128px;">
    <div class="story">
      <p>Quis nostrud exerci tation ullamcorper suscipit lobortis nisl ut aliquip ex ea commodo consequat. Ipsum dolor sit amet consectetuer adipiscing elit sed diam nonummy nibh euismod tincidunt. Demonstraverunt lectores legere me lius quod ii legunt saepius claritas est etiam processus dynamicus qui sequitur.</p>
    </div>
  </section>

  <div class="bar" style="left:356px;top:263px;width:406px;height:43px;"><h2>Ut laoreet dolore magna, aliquam erat</h2></div>
  <section class="panel" style="left:356px;top:306px;width:406px;height:305px;">
    <div class="story">
      <div class="photo" role="img" aria-label="Feature story photograph" style="width:170px;height:148px;"></div>
      <p>Quis nostrud exerci tation ullamcorper suscipit lobortis nisl ut aliquip ex ea commodo consequat. Ipsum dolor sit amet consectetuer adipiscing elit sed diam nonummy nibh euismod tincidunt. Demonstraverunt lectores legere me lius quod ii legunt saepius claritas est etiam processus dynamicus qui sequitur. Quis nostrud exerci tation ullamcorper suscipit lobortis nisl ut aliquip ex ea commodo consequat. Ipsum dolor sit amet consectetuer adipiscing elit sed diam nonummy nibh euismod.</p>
      <p>Quis nostrud exerci tation ullamcorper suscipit lobortis nisl ut aliquip ex ea commodo consequat. Ipsum dolor sit amet consectetuer adipiscing elit sed diam nonummy nibh.</p>
    </div>
  </section>

  <div class="block divider"></div>

  <div class="bar bar--small" style="left:356px;top:619px;width:406px;height:30px;"><h2>Et iusto odio dignissim qui blandit praesent</h2></div>
  <section class="panel" style="left:356px;top:649px;width:406px;height:66px;">
    <ul class="bullets">
      <li>Quis nostrud exerci tation ullamcorper suscipit lobortis nisl ut aliquip ex ea commodo consequat.</li>
      <li>Ipsum dolor sit amet consectetuer adipiscing elit sed diam</li>
    </ul>
  </section>

  <div class="bar bar--small" style="left:356px;top:715px;width:406px;height:29px;"><h2>Ut laoreet dolore magna, aliquam erat</h2></div>
  <section class="panel" style="left:356px;top:744px;width:406px;height:212px;">
    <div class="story story--compact">
      <div class="photo" role="img" aria-label="Story photograph" style="width:170px;height:98px;"></div>
      <p>Quis nostrud exerci tation ullamcorper suscipit lobortis nisl ut aliquip ex ea commodo consequat. Ipsum dolor sit amet consectetuer adipiscing elit sed diam nonummy nibh euismod tincidunt. Demonstraverunt lectores legere me lius quod ii legunt saepius claritas est etiam processus dynamicus qui sequitur. Quis nostrud exerci tation ullamcorper suscipit lobortis nisl ut aliquip ex ea commodo consequat. Ipsum dolor sit amet consectetuer adipiscing elit sed diam nonummy nibh euismod.</p>
      <p>Quis nostrud exerci tation ullamcorper suscipit lobortis nisl ut aliquip ex ea commodo consequat. Ipsum dolor sit amet consectetuer adipiscing elit sed diam nonummy nibh.</p>
    </div>
  </section>

  <div class="bar" style="left:766px;top:90px;width:209px;height:44px;">
    <h2>In This Issue</h2>
    <svg width="26" height="16" viewBox="0 0 26 16" aria-hidden="true">
      <rect x="0.5" y="0.5" width="25" height="15" fill="#f3f4f7" stroke="#9aa3b2"/>
      <path d="M0.5 0.5 L13 9 L25.5 0.5" fill="none" stroke="#9aa3b2"/>
    </svg>
  </div>
  <ul class="block contents">
    <li>Lorem ipsum dolor amet</li>
    <li>Donce imperiat accumsan felis</li>
    <li>Aliquam lectus orci, adipiscing</li>
  </ul>

  <div class="bar" style="left:766px;top:233px;width:209px;height:43px;">
    <h2>Other News</h2>
    <svg width="28" height="22" viewBox="0 0 28 22" aria-hidden="true">
      <path d="M2 20 L14 3 L26 20 Z" fill="#f3f4f7" stroke="#9aa3b2"/>
      <circle cx="14" cy="20" r="2" fill="#c4cad4"/>
    </svg>
  </div>
  <article class="news-item" style="top:277px;height:102px;">
    <h3>Iriure hendrerit insitam quod</h3>
    <p>Et quinta decima eodem modo typi qui nunc nobis videntur parum clari fiant sollemnes in.</p>
  </article>
  <article class="news-item" style="top:379px;height:129px;">
    <h3>Iusto odio dignissim quindit praesent luptatum zzril.</h3>
    <p>Nonummy nibh euismod tincidunt ut laoreet dolore magna aliquam erat! Hendrerit in.</p>
  </article>

  <div class="action" style="top:510px;">
    <span>Forward Email</span>
    <svg width="30" height="16" viewBox="0 0 30 16" aria-hidden="true">
      <rect x="6.5" y="0.5" width="23" height="15" fill="#f3f4f7" stroke="#8a93a3"/>
      <path d="M6.5 0.5 L18 9 L29.5 0.5" fill="none" stroke="#8a93a3"/>
      <path d="M0 6 H8 V3 L13 8 L8 13 V10 H0 Z" fill="#2a3142"/>
    </svg>
  </div>
  <div class="action" style="top:556px;">
    <span>Unsubscribe</span>
    <svg width="30" height="16" viewBox="0 0 30 16" aria-hidden="true">
      <rect x="6.5" y="0.5" width="23" height="15" fill="#f3f4f7" stroke="#8a93a3"/>
      <path d="M6.5 0.5 L18 9 L29.5 0.5" fill="none" stroke="#8a93a3"/>
      <path d="M2 3 L10 12 M10 3 L2 12" stroke="#2a3142" stroke-width="3"/>
    </svg>
  </div>

  <aside class="signup-note">
    You're receiving this newsletter<br>because you signed up at<br>
    <strong>yoursite.com / bought widgets<br>from us.</strong><br>
    Having trouble reading this email?<br>
    <strong>View it in your browser.</strong>
  </aside>

  <footer class="legal">
    Norvale Widgets and the Norvale Widgets Logo are registered trademarks of Norvale Widgets Corp.<br>
    Norvale Widgets Corp - 123 Some Street, City, ST 99999. Ph +1 4 1555 01 742<br>
    Don't want to receive these emails anymore? You can <a href="#">unsubscribe</a>
  </footer>

</div>
</body>
</html>
```